Business Card Design Project

I need a business card design for an Organic drive thru coffee kiosk. We will serve organic coffee, teas & smoothies and will serve healthy breakfast food/snacks for people on the go.
I want the card to have 2-3 colors max (earthy colors like browns, greens and so on).
I have attached the logo I want used and would love to play off the theme of "balance."
Include:
Tidy-Kettle Coffee
address: 4820 Gorvin Ct. Raleigh, NC 27583
phone: 919-731-4062
website: www.tidy-kettle.com (website is not up yet but still include it on card)
email: Rosalind@tidy-kettle.com
I want one of the following sayings somewhere on the card (the front or back is fine):
"Eat & Drink Well, on the run!"
"Break the fast with Tidy-Kettle"
Maybe on the back list what we offer:
-Organic coffee, espresso & tea
-Blendora smoothies & protein shakes
-Zesty Pour (100% fresh local fruit and veggies)
-Tender Nibs

```html
<!DOCTYPE html>
<html lang="en">
<head>
<meta charset="utf-8">
<title>Tidy-Kettle Coffee – Business Card</title>
<link href="https://fonts.googleapis.com/css2?family=Source+Sans+3:wght@400;500&display=swap" rel="stylesheet">
<style>
  :root {
    --paper: #ffffff;
    --earth: #976a43;
    --leaf: #5f8c3f;
    --honey: #e9c41c;
    --sprout: #a6d873;
    --roast: #4a3427;
  }
  html, body {
    margin: 0;
    padding: 0;
    width: 849px;
    height: 1200px;
    overflow: hidden;
    background: var(--paper);
    font-family: "Source Sans 3", sans-serif;
  }
  .sheet {
    position: relative;
    width: 849px;
    height: 1200px;
  }
  .card {
    position: absolute;
    background: var(--earth);
    overflow: hidden;
  }
  .card--front { left: 69px; top: 175px; width: 708px; height: 404px; }
  .card--back  { left: 63px; top: 673px; width: 707px; height: 404px; }

  .brand {
    position: absolute;
    left: 0;
    right: 0;
    display: flex;
    align-items: center;
    justify-content: center;
    gap: 14px;
    color: var(--roast);
    font-weight: 500;
    font-size: 50px;
    letter-spacing: 0.5px;
    line-height: 1;
  }
  .brand__dot {
    width: 22px;
    height: 22px;
    border-radius: 50%;
    background: var(--roast);
  }
  .card--front .brand { top: 142px; }
  .card--back .brand { top: 160px; }

  .offer {
    position: absolute;
    top: 328px;
    margin: 0;
    padding: 0;
    list-style: none;
    color: var(--honey);
    font-size: 18px;
    line-height: 23px;
  }
  .offer--left { left: 29px; }
  .offer--right { right: 30px; text-align: right; }

  .slogan {
    position: absolute;
    top: 27px;
    left: 0;
    right: 0;
    margin: 0;
    text-align: center;
    color: var(--honey);
    font-size: 18px;
    word-spacing: 1px;
  }
  .slogan span + span { margin-left: 22px; }

  .contact {
    position: absolute;
    left: 0;
    right: 0;
    bottom: 0;
    height: 134px;
    background: var(--leaf);
    color: var(--sprout);
    font-size: 16.5px;
  }
  .contact__main {
    position: absolute;
    top: 11px;
    left: 0;
    right: 0;
    text-align: center;
    line-height: 21px;
  }
  .contact__web,
  .contact__mail {
    position: absolute;
    top: 93px;
  }
  .contact__web { left: 45px; }
  .contact__mail { right: 37px; }
</style>
</head>
<body>
<main class="sheet">

  <section class="card card--front" aria-label="Card front">
    <div class="brand"><span class="brand__dot"></span>Tidy-Kettle</div>
    <ul class="offer offer--left">
      <li>Organic Coffee, espresso &amp; tea</li>
      <li>Zesty Pour (100% local fruit &amp; veggies)</li>
    </ul>
    <ul class="offer offer--right">
      <li>Blendora smoothies &amp; protein shakes</li>
      <li>Tender Nibs</li>
    </ul>
  </section>

  <section class="card card--back" aria-label="Card back">
    <p class="slogan"><span>Eat and drink well, on the run !.</span><span>Break the fast, with Tidy-Kettle</span></p>
    <div class="brand"><span class="brand__dot"></span>Tidy-Kettle</div>
    <div class="contact">
      <div class="contact__main">
        Tidy-Kettle Coffee<br>
        address: 4820 Gorvin Ct. Raleigh, NC 27583<br>
        phone: 919-731-4062
      </div>
      <div class="contact__web">website: www.tidy-kettle.com</div>
      <div class="contact__mail">email: Rosalind@tidy-kettle.com</div>
    </div>
  </section>

</main>
</body>
</html>
```